Flyer-Design für Immobilienmakler & Bauträger
Zielgruppe
Wir sind Immobilienmakler & Bauträger
Zielgruppe sind alle, die eine Immobile besitzen und (jetzt oder später) verkaufen möchten
Wir möchten vermehrt Werbung in den lokalen Ortszeitungen machen um bekannter zu werden!
Bei der Vielzahl von Maklern möchten wir hervorstechen und uns auch von den ganzen Franchise Unternhemen abheben
Als kleines Familienunternhemen steht bei uns neben einer erfolgreichen Vermarktung Zuverlässigkeit, Fairness und Freundlichkeit an oberster Stelle!
WOVA (WOhnraum VAldorf) besteht aus
Reinhold Valdorf (Geschäftsführer)
Svenja Valdorf (Tochter)
Jonas Valdorf (Sohn)
Aufgabenstellung
Heidelberg und die Umgebung soll uns als freundliches, zuverlässiges & erfolgreiches Maklerteam kennenlernen, hierfür benötigen wir einen Flyer mit Vorder- und Rückseite
Die Vorderseite soll übersichtlich sein und auf den ersten Blick erkennen lassen
- wer wir sind (gerne auch mit Bildern von uns - diese sollen später von uns durch aktuelle ersetzt werden können)
- was wir suchen (zum Verkauf stehende Objekte - sowohl zur Vermarktung als auch zum Eigenankauf)
- was wir können - bzw was wir tun - Immobilien erfolgreich vermitteln/vermarkeln - für Auftraggeber kostenfrei!!
Gerne auch mit
'Ihr freundliches Immobilienbüro im Herzen von Neuenheim'
Wir haben ebenfalls eine Bauträgergesellschaft, vll könnte man auch dieses Logo mit einfließen lassen
TKR GmbH
Auf der Rückseite soll das Thema Tippgeber aufgegriffen werden -
Ihr Wissen ist bares Geld wert
oder
Wir belohnen Ihr Wissen
Ihre Freunde, Bekannte, Verwandte, Nachbarn oder Vermieter haben Ihnen von Verkaufsplänen ihrer Immobilie erzählt?
Geben Sie den Tipp an uns weiter! Führt dieser zum Verkauf der benannten Immobilie durch uns, ist uns das 10% unserer Maklerprovision (netto) wert.
Und so geht’s:
1. Sie melden sich per E-Mail, Telefon oder über das Homepage-Formular und benennen den Eigentümer und das Objekt, welches verkauft werden soll. Teilen Sie in diesem Rahmen auch mit, ob Ihr Tipp anonym behandelt werden soll.
2. Wir setzen uns mit dem Eigentümer in Verbindung
3. Sie erhalten von uns eine Information
4. Nach erfolgreichen Verkauf erhalten Sie Ihre Tippgeberprovision gutgeschrieben.
Die Tippgebervergütungen werden nach Abschluss der Verträge und nach Eingang der Maklerprovision innerhalb von 7 Tagen ausbezahlt. Bei unterlassener Zahlung der Maklerprovision an uns kann auch keine Auszahlung der Tippgeberprovision erfolgen. Bei mehreren Tipps zu ..

```html
<!DOCTYPE html>
<html lang="de">
<head>
<meta charset="utf-8">
<title>WOVA – Tippgeber Flyer</title>
<link rel="stylesheet" href="https://fonts.googleapis.com/css2?family=Arimo:wght@400;700&display=swap">
<style>
  :root {
    --ink: #1f1f1f;
    --dark: #222222;
    --paper: #ffffff;
    --green: #0b8456;
    --text-dark: #1c1c1c;
  }
  * { margin: 0; padding: 0; box-sizing: border-box; }
  html, body { width: 1200px; height: 846px; overflow: hidden; background: var(--paper); }
  body { font-family: "Arimo", Arial, sans-serif; }
  .flyer { position: relative; width: 1200px; height: 846px; overflow: hidden; background: var(--dark); }
  .backdrop { position: absolute; inset: 0; }
  .accent { color: var(--green); }

  .brand { position: absolute; left: 28px; top: 16px; color: var(--paper); font-weight: 400; }
  .brand-name { font-size: 52px; letter-spacing: 2px; line-height: 1; }
  .brand-sub { font-size: 17px; margin-top: 6px; }
  .brand-tag { font-size: 8px; margin-top: 4px; padding-left: 74px; }

  .intro { position: absolute; left: 24px; top: 128px; width: 370px; color: var(--paper);
           font-size: 15px; line-height: 19.4px; }

  .tip-head { position: absolute; right: 34px; top: 42px; text-align: right; color: var(--text-dark);
              font-size: 19px; font-weight: 700; line-height: 25px; }
  .tip-offer { position: absolute; right: 34px; top: 170px; text-align: right; color: var(--text-dark);
               font-size: 19px; line-height: 24.7px; }

  .since { position: absolute; left: 24px; top: 536px; color: var(--text-dark);
           font-size: 15px; font-weight: 700; line-height: 19.4px; }
  .services { position: absolute; left: 24px; top: 633px; color: var(--text-dark);
              font-size: 15px; line-height: 19.4px; }
  .services strong { font-weight: 700; }
  .slogan { position: absolute; left: 24px; top: 801px; color: var(--green);
            font-size: 15.5px; font-weight: 700; }

  .steps { position: absolute; left: 628px; top: 546px; width: 560px; color: var(--paper);
           font-size: 14.6px; line-height: 19.4px; }
  .steps h2 { font-size: 17px; font-weight: 700; margin-bottom: 6px; }
  .steps ol { list-style: none; }
  .steps .num { color: var(--green); }
  .steps .terms { color: var(--green); }
</style>
</head>
<body>
<main class="flyer">
  <svg class="backdrop" width="1200" height="846" viewBox="0 0 1200 846">
    <defs>
      <linearGradient id="greenFade" x1="0" y1="0" x2="0" y2="1">
        <stop offset="0" stop-color="#0b8456"/>
        <stop offset="0.55" stop-color="#0b7a50"/>
        <stop offset="1" stop-color="#1a2a22"/>
      </linearGradient>
      <linearGradient id="houseTone" x1="0" y1="0" x2="0" y2="1">
        <stop offset="0" stop-color="#c9d6e2"/>
        <stop offset="0.45" stop-color="#a79c8c"/>
        <stop offset="1" stop-color="#4a5a3c"/>
      </linearGradient>
      <linearGradient id="greyTone" x1="0" y1="0" x2="1" y2="1">
        <stop offset="0" stop-color="#8a8a8a"/>
        <stop offset="1" stop-color="#d8d8d8"/>
      </linearGradient>
      <linearGradient id="lightTone" x1="0" y1="0" x2="1" y2="1">
        <stop offset="0" stop-color="#dcdcdc"/>
        <stop offset="1" stop-color="#a9a9a9"/>
      </linearGradient>
    </defs>
    <polygon points="0,300 0,846 543,846" fill="#ffffff"/>
    <polygon points="609,0 1200,0 1200,591" fill="#ffffff"/>

    <polygon points="581,271 733,423 581,575 429,423" fill="url(#greenFade)"/>
    <polygon role="img" aria-label="Foto: Handschlag vor einem Einfamilienhaus"
             points="276,271 428,423 276,575 124,423" fill="url(#houseTone)"/>
    <polygon role="img" aria-label="Porträtfoto Reinhold Valdorf"
             points="429,423 581,575 429,727 277,575" fill="url(#lightTone)"/>
    <polygon role="img" aria-label="Porträtfoto Svenja Valdorf"
             points="734,121 886,273 734,425 582,273" fill="url(#greyTone)"/>
    <polygon role="img" aria-label="Porträtfoto Jonas Valdorf"
             points="886,276 1038,428 886,580 734,428" fill="url(#lightTone)"/>
  </svg>

  <header class="brand">
    <div class="brand-name">WOVA</div>
    <div class="brand-sub">WOhnraum VAldorf</div>
    <div class="brand-tag">Ihr freundliches Immobilienbüro</div>
  </header>

  <p class="intro">Sie möchten Ihre Immobilie verkaufen oder vermieten? Oder suchen Sie eine Immobilie in guter Lage? Als professioneller Immobilienmakler mit der erforderlichen Marktkenntnis beraten wir Sie jederzeit gerne! Überzeugen Sie sich selbst von unserem <span class="accent">exzellenten</span> Service.</p>

  <h1 class="tip-head">Ihre Freunde, Bekannte, Verwandte, Nachbarn<br>oder Vermieter haben Ihnen von<br>Verkaufsplänen ihrer Imobilie<br>erzählt?</h1>

  <p class="tip-offer">Geben Sie den Tipp an uns weiter!<br>Führt dieser zum Verkauf<br>der benannten Imbobile<br>durch uns, ist uns<br>das <span class="accent">10%</span> unserer<br>Maklerprovision<br>wert.</p>

  <p class="since">Seit nunnmehr 20 Jahren<br>stehen wir tfür absolute<br>Professionaltxibilität<br>und Kompetenz.</p>

  <p class="services">Ob Sie den Verkauf, die Vermietung<br>oder den Erwerb einer hochwertigen<br>Altbauwohnung anstreben, in eine<br>Kapitalanlage investieren, Ihre<br>Bestandsimmobilie zeitgemäß sanieren oder<br>diese bewerten lassen möchten – <strong>wir sind Ihr Garant<br>für preisgerechte Immobilien in und um Heidelberg.</strong></p>

  <p class="slogan">Ihr freundliches Immobilienbüro im Herzen von Neuenheim</p>

  <section class="steps">
    <h2>Und so geht`s:</h2>
    <ol>
      <li><span class="num">1.</span> Sie melden sich per E-Mail, Telefon oder über das Hompage-Formular an und benennen den Eigentümer und das Objekt, welches verkauft werden soll. Teilen Sie in diesem Rahmen auch mit, ob Ihr Tipp anonym behandelt werden soll.</li>
      <li><span class="num">2.</span> Wir setzen uns mit dem Eigentümer in Verbindung,</li>
      <li><span class="num">3.</span> Sie erhalten von uns eine Information.</li>
      <li><span class="num">4.</span> Nach erfolgreichen Verkauf erhalten Sie Ihre Tippgeberprovision gutgeschrieben</li>
    </ol>
    <p class="terms">Die Tippgebervergütung werden nach Abschluss der Verträge und nach Eingang der Maklerprovision innerhalb von 7 Tagen ausbezahlt. Bei unterlassener Zahlung der Marklerprovision an uns kann auch keine Auszahlung der Tippgeberprovison erfolgen. Bei mehreren Tipps zu einem Objekt, erhält nur der ersten Tippgeber die Provision</p>
  </section>
</main>
</body>
</html>
```